Eyebrow Tattooist business card design

I am an eyebrow specialist. I wax, shape, tint and tattoo eyebrows. I want a professional but classy image. I like gold raised writing on it. Colour of card either chocolate brown or pale blue??
As I use a technique called feathering and hair strokes, I would like the shape of a eyebrow on the front, with the hair strokes.

Industry/Entity Type
Tattoo
Contact Information for Business Card
I am an eyebrow specialist.
FRONT -  I want the name 'Lush Lids' on the front of the card. With a shape of a brow, with every hair stroke. Need the words 'Tessa brow specialist and cosmetic tattooist' 'using feathered and hairstroke techniques'
03 5162-4730
BACK - At, Serene Glow Spa & Skin Studio. Shop 7, Harlow Grove Plaza, Penfield-Ashbury Road. Penfield East. Vic 3805.
www.lushlids.com.au

```html
<!DOCTYPE html>
<html lang="en">
<head>
<meta charset="utf-8">
<title>Lush Lids – Business Card</title>
<link rel="stylesheet" href="https://fonts.googleapis.com/css2?family=Patrick+Hand&display=swap">
<style>
  :root {
    --page-bg: #e9e6e2;
    --band-black: #0b0b0b;
    --plum-light: #6e3340;
    --plum-mid: #4a1a24;
    --plum-dark: #2a0c12;
    --gold-text: #f1e61c;
    --brow-light: #c9c9c9;
    --brow-dark: #5a5a5a;
    --rule: #1a070b;
  }
  * { margin: 0; padding: 0; box-sizing: border-box; }
  html, body {
    width: 1200px; height: 900px; overflow: hidden;
    background: var(--page-bg);
  }
  .canvas { position: relative; width: 1200px; height: 900px; }
  .card {
    position: absolute; left: 270px;
    width: 660px; height: 377px;
    overflow: hidden;
    background: linear-gradient(180deg, var(--plum-light) 10%, var(--plum-mid) 55%, var(--plum-dark) 100%);
    box-shadow: 0 10px 24px rgba(0,0,0,0.25);
    font-family: "Patrick Hand", cursive;
    color: var(--gold-text);
  }
  .card--front { top: 53px; }
  .card--back  { top: 470px; }
  .band { position: absolute; left: 0; width: 100%; background: var(--band-black); }
  .band--top { top: 0; height: 48px; }
  .band--bottom { bottom: 0; height: 66px; }

  .brand-name {
    position: absolute;
    font-size: 60px; line-height: 1; font-weight: 400;
    color: var(--gold-text);
    white-space: nowrap;
  }
  .brow-art { position: absolute; }

  /* Front */
  .card--front .brand-name { left: 60px; top: 118px; }
  .card--front .brow-art { left: 330px; top: 64px; width: 230px; height: 110px; }
  .details {
    position: absolute; left: 150px; top: 196px;
    text-transform: uppercase; letter-spacing: 0.04em;
  }
  .details .holder { font-size: 24px; line-height: 1.1; }
  .details .line { font-size: 17px; line-height: 1.25; }
  .details .phone { font-size: 22px; line-height: 1.3; letter-spacing: 0.08em; }

  /* Back */
  .card--back .brand-name { left: 120px; top: 96px; font-size: 48px; }
  .card--back .brow-art { left: 300px; top: 70px; width: 130px; height: 66px; }
  .card--back .rule {
    position: absolute; left: 0; top: 154px; width: 100%; height: 1px;
    background: var(--rule);
  }
  .card--back .rule--upper { top: 62px; }
  .venue {
    position: absolute; left: 300px; top: 164px; width: 320px;
    text-align center; text-align: center; font-size: 16px; line-height: 1.22;
  }
  .venue .web { font-size: 17px; margin-bottom: 4px; letter-spacing: 0.02em; }
</style>
</head>
<body>
<main class="canvas">

  <section class="card card--front" aria-label="Business card front">
    <div class="band band--top"></div>
    <div class="band band--bottom"></div>
    <svg class="brow-art" viewBox="0 0 230 110" role="img" aria-label="Eyebrow illustration with feathered hair strokes">
      <defs>
        <linearGradient id="browFront" x1="0" y1="1" x2="1" y2="0">
          <stop offset="0" stop-color="#c9c9c9" stop-opacity="0.55"/>
          <stop offset="1" stop-color="#5a5a5a" stop-opacity="0.55"/>
        </linearGradient>
      </defs>
      <rect width="230" height="110" rx="8" fill="url(#browFront)"/>
    </svg>
    <p class="brand-name">Lush Lids</p>
    <div class="details">
      <p class="holder">Tessa</p>
      <p class="line">‘Brow specialist and cosmetic tattooist’</p>
      <p class="line">‘Using feathered and hairstroke techniques’</p>
      <p class="phone">03 5162-4730</p>
    </div>
  </section>

  <section class="card card--back" aria-label="Business card back">
    <div class="band band--top"></div>
    <div class="band band--bottom"></div>
    <div class="rule rule--upper"></div>
    <svg class="brow-art" viewBox="0 0 130 66" role="img" aria-label="Small eyebrow illustration with hair strokes">
      <defs>
        <linearGradient id="browBack" x1="0" y1="1" x2="1" y2="0">
          <stop offset="0" stop-color="#c9c9c9" stop-opacity="0.5"/>
          <stop offset="1" stop-color="#5a5a5a" stop-opacity="0.5"/>
        </linearGradient>
      </defs>
      <rect width="130" height="66" rx="6" fill="url(#browBack)"/>
    </svg>
    <p class="brand-name">Lush Lids</p>
    <div class="rule"></div>
    <div class="venue">
      <p class="web">www.lushlids.com.au</p>
      <p>At,</p>
      <p>Serene Glow Spa &amp; Skin Studio.</p>
      <p>Shop 7, Harlow Grove Plaza,</p>
      <p>Penfield-Ashbury Road.</p>
      <p>Penfield East. Vic 3805.</p>
    </div>
  </section>

</main>
</body>
</html>
```